We are seeking a package design for our product PURE EARTH BITE. There are 3 different flavours named - Berrino Mocha Boost, Plumly Kern Delight and Rise & Shine Walnut. Our product is Paleo, Gluten Free, Vegan and Raw friendly. We will be using heat sealing Poly Bags approximately 80mmx 120mm.

Target Market(s)

Health conscious individuals

Industry/Entity Type

Health And Wellness

Font styles to use
Sans Serif

Requirements
Must have
• Logo ( front ) - see attachment
• Product name ( front ) 1.see attached
• 2.see attached
• 3.see attached
• Four colour scheme
• Pure Earth Bite ( front )
• 50g ( front )
• Nutritional information ( back ) - 1.see attached
• 2.see attached
• 3.see attached
• Ingredients ( back )
• 1. Almonds, Cranberries, Coconut, Organic Raw Cacao Powder
• 2. Almonds, Figs, Coconut, Cinnamon, Nutmeg
• 3. Almonds, Medjool Dates, Pistachios, Sesame Seeds
• Allergy advice ( back ) Contains Tree Nuts, Sesame Seeds
• Supplier information ( back )
• HAPPY PANTRY BITES
• 41 Larkspur Crescent
• Wodonga 3690 VIC
• tolsen.pty.ltd@brevmail.example
• Storage instructions ( back ) - Store in a cool dry place
• Country of origin ( back ) Made in Australia from local and imported ingredients
• Dimensions and Material 80mm x 120mm Heat Sealing Poly Bags
Nice to have
• Paleo, Gluten Free, Vegan and Raw displayed ( front )

```html
<!DOCTYPE html>
<html lang="en">
<head>
<meta charset="utf-8">
<title>Pure Earth Bite – Flavour Range Packaging</title>
<link rel="stylesheet" href="https://fonts.googleapis.com/css2?family=Arvo:wght@400;700&family=Patrick+Hand&display=swap">
<style>
  :root{
    --stage-top:#d6e3e6;
    --stage-bottom:#e3e6cd;
    --seal:#f4f4f4;
    --seal-edge:#d9d9d9;
    --fig:#d9c63c;
    --cacao:#4b3429;
    --lime:#c2d62b;
    --green:#3b9a2f;
    --green-bright:#5dbb2e;
    --kraft:#bcb6aa;
    --kraft-dark:#a9a397;
    --white:#ffffff;
    --ink:#222222;
    --badge-green:#6aa73a;
    --badge-olive:#5b7b2e;
    --badge-blue:#5aa3b4;
  }
  *{box-sizing:border-box;margin:0;padding:0}
  html,body{width:1200px;height:838px;overflow:hidden}
  body{
    background:linear-gradient(180deg,var(--stage-top) 0%,var(--stage-bottom) 100%);
    position:relative;
    font-family:"Arvo",serif;
  }
  .pack{
    position:absolute;
    display:flex;flex-direction:column;
    filter:drop-shadow(0 6px 8px rgba(0,0,0,.12));
  }
  .pack--fig{left:66px;top:66px;width:328px;height:600px;--body:var(--fig);--s:1}
  .pack--cacao{left:439px;top:77px;width:354px;height:652px;--body:var(--cacao);--s:1.08}
  .pack--walnut{left:836px;top:66px;width:328px;height:600px;--body:var(--lime);--s:1}

  .seal{
    height:48px;flex:none;position:relative;
    background:
      repeating-linear-gradient(180deg,var(--seal) 0 3px,var(--seal-edge) 3px 4px);
  }
  .seal--top{
    clip-path:polygon(0 6px,2% 0,4% 6px,6% 0,8% 6px,10% 0,12% 6px,14% 0,16% 6px,18% 0,20% 6px,22% 0,24% 6px,26% 0,28% 6px,30% 0,32% 6px,34% 0,36% 6px,38% 0,40% 6px,42% 0,44% 6px,46% 0,48% 6px,50% 0,52% 6px,54% 0,56% 6px,58% 0,60% 6px,62% 0,64% 6px,66% 0,68% 6px,70% 0,72% 6px,74% 0,76% 6px,78% 0,80% 6px,82% 0,84% 6px,86% 0,88% 6px,90% 0,92% 6px,94% 0,96% 6px,98% 0,100% 6px,100% 100%,0 100%);
  }
  .seal--bottom{
    clip-path:polygon(0 0,100% 0,100% calc(100% - 6px),98% 100%,96% calc(100% - 6px),94% 100%,92% calc(100% - 6px),90% 100%,88% calc(100% - 6px),86% 100%,84% calc(100% - 6px),82% 100%,80% calc(100% - 6px),78% 100%,76% calc(100% - 6px),74% 100%,72% calc(100% - 6px),70% 100%,68% calc(100% - 6px),66% 100%,64% calc(100% - 6px),62% 100%,60% calc(100% - 6px),58% 100%,56% calc(100% - 6px),54% 100%,52% calc(100% - 6px),50% 100%,48% calc(100% - 6px),46% 100%,44% calc(100% - 6px),42% 100%,40% calc(100% - 6px),38% 100%,36% calc(100% - 6px),34% 100%,32% calc(100% - 6px),30% 100%,28% calc(100% - 6px),26% 100%,24% calc(100% - 6px),22% 100%,20% calc(100% - 6px),18% 100%,16% calc(100% - 6px),14% 100%,12% calc(100% - 6px),10% 100%,8% calc(100% - 6px),6% 100%,4% calc(100% - 6px),2% 100%,0 calc(100% - 6px));
  }
  .hang-hole{
    position:absolute;left:50%;top:18px;width:14px;height:14px;margin-left:-7px;
    border-radius:50%;background:var(--stage-top);border:1px solid #c8c8c8;
  }
  .pack__body{flex:1;position:relative;background:var(--body);overflow:hidden}
  .base{position:absolute;inset:0;width:100%;height:100%}

  .brand{
    position:absolute;left:50%;top:6%;transform:translateX(-50%);
    width:calc(156px * var(--s));height:calc(48px * var(--s));
    border-radius:50%;background:var(--white);
    border:3px solid var(--green-bright);
    display:flex;align-items:center;justify-content:center;
    font-family:"Arvo",serif;font-weight:400;color:var(--green);
    font-size:calc(11px * var(--s));letter-spacing:.06em;text-align:center;line-height:1.1;
  }
  .title{
    position:absolute;left:0;right:0;top:22%;
    text-align:center;color:var(--white);
    font-family:"Arvo",serif;font-weight:700;
    font-size:calc(27px * var(--s));line-height:1.25;letter-spacing:.01em;
    text-shadow:0 1px 0 rgba(0,0,0,.15);
  }
  .tagline{
    position:absolute;left:0;right:0;top:40%;text-align:center;
    font-family:"Arvo",serif;font-weight:700;color:var(--green);
    font-size:calc(22px * var(--s));
  }
  .pack--cacao .tagline{color:var(--green-bright)}
  .tagline::after{
    content:"";display:block;width:calc(224px * var(--s));height:2px;margin:4px auto 0;
    background:currentColor;
  }
  .callout{
    position:absolute;left:14%;top:58%;
    font-family:"Patrick Hand",sans-serif;color:var(--white);
    font-size:calc(14px * var(--s));line-height:1.15;
  }
  .callout svg{position:absolute;left:100%;top:2px;margin-left:4px}
  .ball{
    position:absolute;left:66%;top:63%;transform:translate(-50%,-50%);
    width:calc(96px * var(--s));height:calc(96px * var(--s));border-radius:50%;
  }
  .pack--fig .ball{background:radial-gradient(circle at 40% 35%,#e0b87a,#b9863f 70%,#8f6428)}
  .pack--cacao .ball{background:radial-gradient(circle at 40% 35%,#8d7a80,#4a3a3e 70%,#2c2124)}
  .pack--walnut .ball{background:radial-gradient(circle at 40% 35%,#f4f3dc,#c9cba4 65%,#9fa47a)}

  .claims{
    position:absolute;left:0;right:0;top:84%;
    display:flex;justify-content:center;gap:calc(12px * var(--s));
  }
  .claim{width:calc(40px * var(--s));height:calc(40px * var(--s));border-radius:50%}
  .claim--vegan{background:var(--badge-green)}
  .claim--paleo{background:var(--badge-olive)}
  .claim--raw{background:var(--badge-green);border-radius:50%/50%;height:calc(26px * var(--s));align-self:center;width:calc(44px * var(--s))}
  .claim--gluten{background:var(--badge-blue);border:2px solid var(--white)}
  .net{
    position:absolute;left:0;right:0;bottom:2.2%;text-align:center;
    font-family:"Arvo",serif;font-size:calc(11px * var(--s));color:var(--ink);
  }
</style>
</head>
<body>

<section class="pack pack--fig" aria-label="Plumly Kern Delight pack">
  <div class="seal seal--top"><span class="hang-hole"></span></div>
  <div class="pack__body">
    <svg class="base" viewBox="0 0 100 100" preserveAspectRatio="none" aria-hidden="true">
      <path d="M0,84 Q55,94 100,56 L100,61 Q55,99 0,89 Z" fill="var(--green-bright)"/>
      <path d="M0,88 Q55,98 100,60 L100,100 L0,100 Z" fill="var(--kraft)"/>
    </svg>
    <div class="brand">HAPPY PANTRY<br>BITES</div>
    <h2 class="title">PLUMLY KERN<br>DELIGHT</h2>
    <p class="tagline">Pure Earth Bite</p>
    <p class="callout">A TASTE<br>OF REAL FOOD
      <svg width="34" height="12" viewBox="0 0 34 12" aria-hidden="true"><path d="M1,4 Q16,12 31,6 M26,2 L31,6 L26,10" fill="none" stroke="#fff" stroke-width="1.5"/></svg>
    </p>
    <div class="ball" role="img" aria-label="Photo of a fig and nut energy ball"></div>
    <div class="claims">
      <span class="claim claim--vegan" role="img" aria-label="Vegan claim badge"></span>
      <span class="claim claim--paleo" role="img" aria-label="Paleo friendly badge"></span>
      <span class="claim claim--raw" role="img" aria-label="Raw badge"></span>
      <span class="claim claim--gluten" role="img" aria-label="Gluten free badge"></span>
    </div>
    <p class="net">net 50gr</p>
  </div>
  <div class="seal seal--bottom"></div>
</section>

<section class="pack pack--cacao" aria-label="Berrino Mocha Boost pack">
  <div class="seal seal--top"><span class="hang-hole"></span></div>
  <div class="pack__body">
    <svg class="base" viewBox="0 0 100 100" preserveAspectRatio="none" aria-hidden="true">
      <path d="M0,75 Q55,80 100,58 L100,63 Q55,85 0,80 Z" fill="var(--green-bright)"/>
      <path d="M0,79 Q55,84 100,62 L100,100 L0,100 Z" fill="var(--kraft)"/>
    </svg>
    <div class="brand">HAPPY PANTRY<br>BITES</div>
    <h2 class="title">BERRINO<br>MOCHA BOOST</h2>
    <p class="tagline">Pure Earth Bite</p>
    <p class="callout" style="top:59%">A TASTE<br>OF REAL FOOD
      <svg width="36" height="12" viewBox="0 0 34 12" aria-hidden="true"><path d="M1,4 Q16,12 31,6 M26,2 L31,6 L26,10" fill="none" stroke="#fff" stroke-width="1.5"/></svg>
    </p>
    <div class="ball" role="img" aria-label="Photo of a cacao energy ball rolled in coconut" style="top:66%"></div>
    <div class="claims">
      <span class="claim claim--vegan" role="img" aria-label="Vegan claim badge"></span>
      <span class="claim claim--paleo" role="img" aria-label="Paleo friendly badge"></span>
      <span class="claim claim--raw" role="img" aria-label="Raw badge"></span>
      <span class="claim claim--gluten" role="img" aria-label="Gluten free badge"></span>
    </div>
    <p class="net">net 50gr</p>
  </div>
  <div class="seal seal--bottom"></div>
</section>

<section class="pack pack--walnut" aria-label="Rise &amp; Shine Walnut pack">
  <div class="seal seal--top"><span class="hang-hole"></span></div>
  <div class="pack__body">
    <svg class="base" viewBox="0 0 100 100" preserveAspectRatio="none" aria-hidden="true">
      <path d="M0,84 Q55,94 100,56 L100,61 Q55,99 0,89 Z" fill="var(--green)"/>
      <path d="M0,88 Q55,98 100,60 L100,100 L0,100 Z" fill="var(--kraft)"/>
    </svg>
    <div class="brand">HAPPY PANTRY<br>BITES</div>
    <h2 class="title">RISE &amp; SHINE<br>WALNUT</h2>
    <p class="tagline">Pure Earth Bite</p>
    <p class="callout">A TASTE<br>OF REAL FOOD
      <svg width="34" height="12" viewBox="0 0 34 12" aria-hidden="true"><path d="M1,4 Q16,12 31,6 M26,2 L31,6 L26,10" fill="none" stroke="#fff" stroke-width="1.5"/></svg>
    </p>
    <div class="ball" role="img" aria-label="Photo of a walnut energy ball coated in sesame seeds"></div>
    <div class="claims">
      <span class="claim claim--vegan" role="img" aria-label="Vegan claim badge"></span>
      <span class="claim claim--paleo" role="img" aria-label="Paleo friendly badge"></span>
      <span class="claim claim--raw" role="img" aria-label="Raw badge"></span>
      <span class="claim claim--gluten" role="img" aria-label="Gluten free badge"></span>
    </div>
    <p class="net">net 50gr</p>
  </div>
  <div class="seal seal--bottom"></div>
</section>

</body>
</html>
```